Velmora Junior Reading & Counting Drive

Development of the (VJRCD) website. The Velmora Junior Reading and Counting Drive (VJRCD) is a Velmora Office of Schooling Project running in approximately 810 participating Gauteng Primary Schools. The project goals are to improve Language and Mathematics scores in participating schools.
The colors should be the same colors as Velmora Schooling office colors ( see logos)

Try bring in human element - this project is about improving literacy and numeracy levels of marginalized primary school children.

Target Market(s)

Education sector and general public

Industry/Entity Type

School

Requirements
Must have
• The primary navigation of the site must always be displayed on each page.
? Each section must have a main page where visitors can navigate to the sub items under the relevant section.
? The overall design concept for the website must be optimised in terms of brand identity, accessibility, usability and content distribution. Colours and images must be chosen according to VJRCD’s corporate identity requirements.
? The VJRCD’s logo should be present on the homepage and visible at all times during a person’s visit.

```html
<!DOCTYPE html>
<html lang="en">
<head>
<meta charset="utf-8">
<title>Velmora Junior Reading &amp; Counting Drive</title>
<link rel="stylesheet" href="https://fonts.googleapis.com/css2?family=Ubuntu:wght@400;500;700&family=Arimo:wght@400;700&display=swap">
<style>
:root{
  --navy:#2d3e84;
  --navy-deep:#23326f;
  --navy-dark:#1b2660;
  --orange:#f0a30a;
  --orange-soft:#f6b53a;
  --cream:#f7f2e8;
  --news-bg:#fdf8ec;
  --text-grey:#8a8a8a;
  --text-dark:#333;
  --title-blue:#1a5aa6;
  --white:#fff;
}
*{box-sizing:border-box;margin:0;padding:0}
html,body{width:1000px;height:1200px;overflow:hidden}
body{position:relative;background:var(--cream);font-family:Arimo,Arial,sans-serif;color:var(--text-dark)}
.abs{position:absolute}

/* top bar */
.top-bar{left:0;top:0;width:1000px;height:36px;background:linear-gradient(var(--navy),var(--navy-deep));border-bottom:3px solid var(--orange)}
.top-links{left:40px;top:9px;display:flex;gap:16px;font-family:Ubuntu,sans-serif;font-size:13px;color:var(--white)}

/* header */
.header{left:0;top:39px;width:1000px;height:148px;background:var(--white);border-bottom:3px solid var(--orange)}
.org-mark{left:44px;top:100px;display:flex;align-items:center;gap:12px}
.org-mark .dot{width:44px;height:44px;border-radius:50%;background:var(--navy)}
.org-mark .name{font-family:Ubuntu,sans-serif;font-weight:500;font-size:20px;color:var(--title-blue)}
.contact-pill{left:487px;width:300px;height:68px;border-radius:34px;background:linear-gradient(90deg,#eeeeee,#ffffff 80%)}
.contact-pill.call{top:42px}
.contact-pill.mail{top:112px}
.contact-pill svg{position:absolute;left:28px;top:20px}
.contact-label{position:absolute;left:80px;top:18px;font-family:Arimo,sans-serif;font-size:14px;color:var(--orange)}
.contact-value{position:absolute;left:80px;top:36px;font-family:Arimo,sans-serif;font-weight:700;font-size:19px;color:var(--navy-dark)}
.site-mark{left:760px;top:5px;width:190px;height:180px;border-radius:95px 95px 0 0;background:var(--white);display:flex;flex-direction:column;align-items:center;justify-content:center;gap:10px}
.site-mark .dot{width:54px;height:54px;border-radius:50%;background:var(--orange)}
.site-mark .name{font-family:Ubuntu,sans-serif;font-weight:700;font-size:30px;color:var(--navy)}

/* nav */
.nav-band{left:0;top:189px;width:1000px;height:160px;background:linear-gradient(var(--navy) 0,var(--navy) 30%,var(--navy-deep))}
.main-nav{left:40px;top:189px;width:920px;height:46px;display:flex}
.main-nav a{flex:auto;display:flex;align-items:center;justify-content:center;font-family:Ubuntu,sans-serif;font-size:14px;color:var(--white);text-decoration:none;border-right:1px solid rgba(0,0,0,.25);box-shadow:1px 0 0 rgba(255,255,255,.08)}
.main-nav a:last-child{border-right:none}

/* slider */
.slider{left:40px;top:235px;width:922px;height:317px;border:3px solid var(--orange);border-radius:5px;background:var(--white);overflow:hidden}
.slide-photo{width:100%;height:100%;background:radial-gradient(ellipse at 62% 45%,#c98d66 0,#8a6048 18%,transparent 32%),linear-gradient(90deg,#c9c2b8,#5a5a5e 25%,#dcd8d0 50%,#2c3556 78%,#a89b86)}
.slider-tab{left:420px;top:524px;width:162px;height:26px;background:var(--orange);border-radius:10px 10px 0 0;display:flex;justify-content:center;align-items:center;gap:4px}
.slider-tab span{width:5px;height:5px;border-radius:50%;background:var(--white)}

/* content */
.content{left:30px;top:552px;width:940px;height:506px;background:var(--white)}
.welcome-title{left:49px;top:577px;width:560px;font-family:Ubuntu,sans-serif;font-weight:400;font-size:24px;line-height:29px;color:#111}
.welcome-title strong{font-weight:500;color:var(--title-blue)}
.welcome-text{left:49px;top:652px;width:625px;font-size:12.5px;line-height:19px;color:var(--text-grey)}

.feature-wrap{left:42px;top:744px;width:641px;height:295px;border:1px solid #ddd;box-shadow:0 0 3px rgba(0,0,0,.12)}
.feature{top:749px;width:315px;height:284px}
.feature.projects{left:47px;background:var(--navy)}
.feature.districts{left:362px;background:var(--orange)}
.feature h2{position:absolute;left:10px;top:10px;font-family:Ubuntu,sans-serif;font-weight:400;font-size:22px;color:var(--white)}
.feature-body{position:absolute;left:10px;top:48px;width:296px;height:226px;background:var(--white);padding:12px 4px 0 13px;font-size:11.5px;line-height:19.2px;color:#444}
.feature-text{height:176px;overflow:hidden}
.more-btn{position:absolute;left:13px;top:193px;padding:1px 8px;font-size:12px;font-weight:700;color:var(--white);border-radius:2px}
.projects .more-btn{background:var(--navy-dark)}
.districts .more-btn{background:var(--orange-soft)}

/* news */
.news{left:698px;top:581px;width:264px;height:452px;background:var(--news-bg);border:1px solid #e6dcc6;border-radius:4px}
.news-head{position:absolute;left:18px;top:16px;width:226px;height:30px;border-bottom:1px solid #ddd}
.news-head h2{font-family:Ubuntu,sans-serif;font-weight:400;font-size:19px;color:#111}
.view-all{position:absolute;right:0;top:6px;font-size:10px;color:#999;letter-spacing:.3px}
.news-item{position:absolute;left:18px;width:226px;height:97px;border-bottom:1px dotted #ccc}
.news-date{position:absolute;left:2px;top:0;width:52px;height:52px;border-radius:0 50% 50% 50%;background:var(--orange);color:var(--white);text-align:center;font-family:Georgia,serif}
.news-date b{display:block;font-size:17px;line-height:18px;padding-top:3px}
.news-date i{display:block;font-style:normal;font-family:Arimo,sans-serif;font-size:11px;line-height:12px}
.news-item h3{position:absolute;left:71px;top:-2px;font-size:12.5px;font-weight:700;color:#333}
.news-item p{position:absolute;left:71px;top:15px;width:152px;font-size:12px;line-height:15.5px;color:#333}

/* footer */
.footer{left:0;top:1058px;width:1000px;height:142px;background:var(--navy);border-top:3px solid var(--orange)}
.footer h2{position:absolute;top:28px;font-family:Ubuntu,sans-serif;font-weight:400;font-size:18px;color:var(--white)}
.footer ul{position:absolute;top:61px;list-style:none;font-size:12px;line-height:19.5px;color:var(--white)}
.social{position:absolute;left:776px;top:61px;display:flex;gap:12px}
.social span{width:30px;height:30px;border-radius:4px;background:rgba(255,255,255,.85)}
</style>
</head>
<body>

<div class="abs top-bar"></div>
<nav class="abs top-links"><span>HOME</span><span>ABOUT THE VJRCD</span><span>MANAGEMENT TEAMS</span><span>CONTACT THE VJRCD</span></nav>

<header class="abs header"></header>
<div class="abs org-mark"><span class="dot"></span><span class="name">Velmora Office of Schooling</span></div>

<div class="abs contact-pill call">
  <svg width="34" height="34" viewBox="0 0 24 24"><path fill="#e0955a" d="M6.6 10.8c1.4 2.8 3.8 5.1 6.6 6.6l2.2-2.2c.3-.3.7-.4 1-.2 1.1.4 2.3.6 3.6.6.6 0 1 .4 1 1V20c0 .6-.4 1-1 1C10.6 21 3 13.4 3 4c0-.6.4-1 1-1h3.5c.6 0 1 .4 1 1 0 1.3.2 2.5.6 3.6.1.3 0 .7-.2 1z"/></svg>
  <span class="contact-label">CALL US ON</span>
  <span class="contact-value">071 555 0148</span>
</div>
<div class="abs contact-pill mail">
  <svg width="34" height="28" viewBox="0 0 34 28"><rect x="1" y="3" width="32" height="22" rx="2" fill="#e0955a"/><path d="M2 5l15 11L32 5" fill="none" stroke="#fff" stroke-width="2"/></svg>
  <span class="contact-label">EMAIL</span>
  <span class="contact-value">hello@vjrcd.org</span>
</div>

<div class="abs site-mark"><span class="dot"></span><span class="name">VJRCD</span></div>

<div class="abs nav-band"></div>
<nav class="abs main-nav">
  <a>PROJECT</a><a>LATEST NEWS</a><a>STRUCTURE</a><a>GOALS</a><a>CONSULTANTS</a><a>SERVICE PROVIDERS</a><a>DISTRICT INVOLMENT</a>
</nav>

<div class="abs slider"><div class="slide-photo" role="img" aria-label="Photo of smiling primary school pupils in a classroom"></div></div>
<div class="abs slider-tab"><span></span><span></span><span></span><span></span><span></span><span></span><span></span><span></span><span></span><span></span></div>

<main class="abs content"></main>
<h1 class="abs welcome-title">Welcome to&nbsp; <strong>Velmora Junior Reading &amp; Counting Drive</strong></h1>
<p class="abs welcome-text">Lorem ipsum dolor sit amet, consectetur adipisicing elit, sed do eiusmod tempor incididunt ut labore et dolore magna aliqua. Ut enim ad minim veniam, quis nostrud exercitation ullamco laboris nisi ut aliquip ex ea commodo consequat. Duis aute irure dolor in reprehenderit in voluptate velit esse cillum dolore eu fugiat nulla pariatur. Excepteur sint occaecat cupidatat non proident, sunt in culpa qui officia deserunt mollit anim id est laborum.</p>

<div class="abs feature-wrap"></div>
<section class="abs feature projects">
  <h2>Projects</h2>
  <div class="feature-body"><p class="feature-text">Lorem ipsum dolor sit amet, consectetur adipisicing elit, sed do eiusmod tempor incididunt ut labore et dolore magna aliqua. Ut enim ad minim veniam, quis nostrud exercitation ullamco laboris nisi ut aliquip ex ea commodo consequat. Duis aute irure dolor in reprehenderit in voluptate velit esse cillum dolore eu fugiat nulla pariatur. Excepteur sint occaecat cupidatat non proident, sunt in culpa qui officia deserunt mollit anim id est laborum</p>
    <span class="more-btn">More</span></div>
</section>
<section class="abs feature districts">
  <h2>District Involvements</h2>
  <div class="feature-body"><p class="feature-text">Lorem ipsum dolor sit amet, consectetur adipisicing elit, sed do eiusmod tempor incididunt ut labore et dolore magna aliqua. Ut enim ad minim veniam, quis nostrud exercitation ullamco laboris nisi ut aliquip ex ea commodo consequat. Duis aute irure dolor in reprehenderit in voluptate velit esse cillum dolore eu fugiat nulla pariatur. Excepteur sint occaecat cupidatat non proident, sunt in culpa qui officia deserunt mollit anim id est laborum</p>
    <span class="more-btn">More</span></div>
</section>

<aside class="abs news">
  <div class="news-head"><h2>News</h2><span class="view-all">VIEW ALL &#9656;</span></div>
  <article class="news-item" style="top:56px"><div class="news-date"><b>31</b><i>APR</i><i>2011</i></div><h3>Lorem ipsum dolor sit</h3><p>Lorem ipsum dolor sit amet, consectetur adipisicing elit, sed do eiusmod...</p></article>
  <article class="news-item" style="top:153px"><div class="news-date"><b>31</b><i>APR</i><i>2011</i></div><h3>Lorem ipsum dolor sit</h3><p>Lorem ipsum dolor sit amet, consectetur adipisicing elit, sed do eiusmod...</p></article>
  <article class="news-item" style="top:250px"><div class="news-date"><b>31</b><i>APR</i><i>2011</i></div><h3>Lorem ipsum dolor sit</h3><p>Lorem ipsum dolor sit amet, consectetur adipisicing elit, sed do eiusmod...</p></article>
  <article class="news-item" style="top:347px;border-bottom:none"><div class="news-date"><b>31</b><i>APR</i><i>2011</i></div><h3>Lorem ipsum dolor sit</h3><p>Lorem ipsum dolor sit amet, consectetur adipisicing elit, sed do eiusmod...</p></article>
</aside>

<footer class="abs footer">
  <h2 style="left:59px">Quick Links</h2>
  <ul style="left:60px"><li>Home</li><li>About the VJRCD</li><li>Management Team</li></ul>
  <ul style="left:193px"><li>Latest News</li><li>Support</li><li>Contact The VJRCD</li></ul>
  <h2 style="left:396px">Our Location</h2>
  <ul style="left:397px"><li>Naledi Osei</li><li>42 Larkspur Avenue,</li><li>Velmora, 4102</li></ul>
  <ul style="left:559px"><li>Phone: 012 555 0190</li><li>Fax: 012 555 0191</li><li>Cell: 071 555 0148</li></ul>
  <h2 style="left:775px">Social Network</h2>
  <div class="social" aria-label="Social network links"><span></span><span></span><span></span><span></span></div>
</footer>

</body>
</html>
```